Brookmere Osteopathy flyer

I want a clean clear DL flyer (but also want an A4 poster) promoting a new Osteopathic business in a semi rural area in Tasmania (Australia).
It can have pictures like the examples attached to show people what Osteopathy is (its like Chiropractic and physiotherapy).
I am the sole practioner and am male, so any pictures would be best to be a white male if possible.
I've attached some wording, you can use all, or none of it
I don't have a phone number for the business yet
info@brookmereosteopathy.example
www.brookmereosteopathy.example
Target Market(s)
Australians, from tradies, professionals, babies to retired people
Industry/Entity Type
Health
Look and feel

```html
<!DOCTYPE html>
<html lang="en">
<head>
<meta charset="utf-8">
<title>Brookmere Osteopathy – Flyer</title>
<link rel="stylesheet" href="https://fonts.googleapis.com/css2?family=Montserrat:ital,wght@0,500;0,600;0,700;1,400;1,700&family=Poppins:wght@400&display=swap">
<style>
  :root{
    --stage:#4f4f4f;
    --paper:#ffffff;
    --blue-light:#3bb8ec;
    --blue-mid:#2a86d0;
    --blue-deep:#1f5fb0;
    --blue-column:#174f96;
    --orange:#f28a2e;
    --text-dark:#2b2b2b;
    --logo-blue:#2a8fd6;
  }
  *{margin:0;padding:0;box-sizing:border-box}
  html,body{width:678px;height:1200px;overflow:hidden;background:var(--stage)}
  .flyer{position:absolute;left:89px;top:72px;width:498px;height:1057px;overflow:hidden;background:var(--paper)}
  .flyer-shapes{position:absolute;inset:0;width:498px;height:1057px}
  .intro{position:absolute;left:9px;top:583px;width:180px;text-align:center;
    font-family:"Montserrat",sans-serif;font-style:italic;font-weight:400;font-size:16px;line-height:22px;color:#fff}
  .intro strong{color:var(--orange);font-weight:700}
  .reasons-title{position:absolute;left:77px;top:620px;width:320px;transform:rotate(-90deg);text-align:center;
    font-family:"Montserrat",sans-serif;font-weight:600;font-size:24px;line-height:29px;color:#fff}
  .condition{position:absolute;width:120px;text-align:center;font-family:"Montserrat",sans-serif;
    font-weight:500;font-size:13.5px;line-height:16px;color:#fff}
  .brand{position:absolute;left:27px;top:897px;width:144px;height:144px;border-radius:50%;background:#fff;
    box-shadow:0 2px 8px rgba(0,0,0,.18);display:flex;align-items:center;justify-content:center;text-align:center;
    font-family:"Montserrat",sans-serif;font-weight:600;font-size:15px;line-height:19px;color:var(--logo-blue)}
  .call-pill{position:absolute;left:190px;top:936px;width:280px;height:30px;border-radius:15px;background:var(--orange);
    font-family:"Montserrat",sans-serif;font-weight:700;font-size:17px;line-height:30px;color:#fff;padding-left:15px}
  .contact{position:absolute;left:197px;font-family:"Poppins",sans-serif;font-size:14px;line-height:18px;color:var(--text-dark);
    display:flex;align-items:center;gap:5px;white-space:nowrap}
  .contact svg{width:13px;height:13px;flex:none}
</style>
</head>
<body>
<main class="flyer">
  <svg class="flyer-shapes" viewBox="0 0 1070 2270" preserveAspectRatio="none" aria-hidden="false">
    <defs>
      <linearGradient id="blueField" x1="0" y1="0" x2="0" y2="1">
        <stop offset="0" stop-color="var(--blue-light)"/>
        <stop offset=".35" stop-color="var(--blue-mid)"/>
        <stop offset="1" stop-color="var(--blue-deep)"/>
      </linearGradient>
      <linearGradient id="columnShade" x1="0" y1="0" x2="0" y2="1">
        <stop offset="0" stop-color="var(--blue-column)" stop-opacity=".25"/>
        <stop offset=".5" stop-color="var(--blue-column)" stop-opacity=".75"/>
        <stop offset="1" stop-color="var(--blue-column)" stop-opacity=".55"/>
      </linearGradient>
      <linearGradient id="photoTone" x1="0" y1="0" x2="1" y2="1">
        <stop offset="0" stop-color="#e9e6e3"/>
        <stop offset=".45" stop-color="#c99c82"/>
        <stop offset="1" stop-color="#2c3b5e"/>
      </linearGradient>
      <linearGradient id="skinTone" x1="0" y1="0" x2="1" y2="1">
        <stop offset="0" stop-color="#f1e6dd"/>
        <stop offset="1" stop-color="#d9a98a"/>
      </linearGradient>
      <linearGradient id="footerTint" x1="0" y1="0" x2="0" y2="1">
        <stop offset="0" stop-color="#e8e8ea"/>
        <stop offset=".35" stop-color="#ffffff"/>
      </linearGradient>
      <clipPath id="clipTreatmentA"><circle cx="390" cy="820" r="188"/></clipPath>
      <clipPath id="clipTreatmentB"><circle cx="908" cy="493" r="155"/></clipPath>
    </defs>

    <g role="img" aria-label="Photo: osteopath treating a patient's lower back on a treatment table">
      <path d="M0,0 H1070 V115 C880,380 560,560 0,685 Z" fill="url(#photoTone)"/>
    </g>

    <path class="blue-field" d="M0,1230 C320,980 640,700 1070,580 V2270 H0 Z" fill="url(#blueField)"/>
    <path class="accent-curve" d="M20,1210 C120,1120 160,1060 190,990" fill="none" stroke="var(--blue-mid)" stroke-width="14" stroke-linecap="round"/>

    <rect class="title-column" x="420" y="1045" width="180" height="900" fill="url(#columnShade)"/>

    <circle cx="390" cy="820" r="203" fill="#fff" stroke="var(--orange)" stroke-width="30"/>
    <g role="img" aria-label="Photo: osteopath's hands working on a patient's shoulder and neck" clip-path="url(#clipTreatmentA)">
      <rect x="200" y="630" width="380" height="380" fill="url(#skinTone)"/>
    </g>

    <circle cx="908" cy="493" r="170" fill="#fff" stroke="var(--orange)" stroke-width="30"/>
    <g role="img" aria-label="Photo: osteopath applying pressure to a patient's lower back" clip-path="url(#clipTreatmentB)">
      <rect x="750" y="335" width="320" height="320" fill="url(#skinTone)"/>
    </g>

    <g class="condition-icons" fill="none" stroke="#fff" stroke-width="3">
      <circle cx="708" cy="785" r="62" role="img" aria-label="Icon: back and neck pain"/>
      <circle cx="917" cy="785" r="62" role="img" aria-label="Icon: headache"/>
      <circle cx="708" cy="1020" r="62" role="img" aria-label="Icon: knee joint"/>
      <circle cx="917" cy="1020" r="62" role="img" aria-label="Icon: spinal disc"/>
      <circle cx="708" cy="1245" r="62" role="img" aria-label="Icon: pregnancy"/>
      <circle cx="917" cy="1255" r="62" role="img" aria-label="Icon: sciatic nerve"/>
      <circle cx="708" cy="1505" r="62" role="img" aria-label="Icon: foot"/>
      <circle cx="917" cy="1505" r="62" role="img" aria-label="Icon: tendon"/>
      <circle cx="713" cy="1735" r="62" role="img" aria-label="Icon: frozen shoulder"/>
      <circle cx="922" cy="1735" r="62" role="img" aria-label="Icon: racquet and elbow"/>
    </g>

    <path class="footer-accent" d="M0,1890 C150,1815 330,1825 460,1905 C300,1855 150,1880 0,1965 Z" fill="var(--orange)"/>
    <path class="footer-accent" d="M870,2005 C960,1978 1020,1940 1070,1918 V1955 C1010,1980 950,2000 870,2005 Z" fill="var(--orange)"/>
    <path class="footer-panel" d="M0,1935 C150,1860 330,1870 500,1945 C650,2005 800,2040 900,2010 C980,1990 1030,1968 1070,1952 V2270 H0 Z" fill="url(#footerTint)"/>
  </svg>

  <p class="intro">Osteopaths use<br>a combination of<br><strong>joint manipulation,<br>targeted deep<br>tissue massage</strong><br>and <strong>stretching</strong> to<br>improve <strong>function,<br>relieve pain</strong> and<br>support the body’s<br>ability to <strong>heal<br>itself.</strong></p>

  <h1 class="reasons-title">Common reasons<br>people visit an osteopath</h1>

  <p class="condition" style="left:270px;top:398px">Back<br>/ neck pain</p>
  <p class="condition" style="left:367px;top:398px">Headaches<br>/ migraines</p>
  <p class="condition" style="left:270px;top:508px">Joint and<br>muscle pain</p>
  <p class="condition" style="left:367px;top:508px">Disc related<br>issues</p>
  <p class="condition" style="left:272px;top:614px">Pregnancy<br>related<br>discomfort</p>
  <p class="condition" style="left:369px;top:617px">Sciatica</p>
  <p class="condition" style="left:269px;top:735px">Plantar<br>fasciitis</p>
  <p class="condition" style="left:369px;top:735px">Tendonitis<br>/ Bursitis</p>
  <p class="condition" style="left:272px;top:841px">Adhesive<br>capsulitis<br>(frozen<br>shoulder)</p>
  <p class="condition" style="left:369px;top:841px">Tennis<br>/ Golfers<br>elbow</p>

  <div class="brand">Brookmere<br>Osteopathy</div>

  <p class="call-pill">Call us Today! 555-014-272</p>

  <p class="contact" style="top:973px">
    <svg viewBox="0 0 24 24" aria-hidden="true"><path d="M12 2a7 7 0 0 0-7 7c0 5 7 13 7 13s7-8 7-13a7 7 0 0 0-7-7z" fill="var(--orange)"/><circle cx="12" cy="9" r="2.6" fill="#fff"/></svg>
    27 Willow Bend road, Brookmere</p>
  <p class="contact" style="top:991px">
    <svg viewBox="0 0 24 24" aria-hidden="true"><rect x="2" y="5" width="20" height="14" fill="none" stroke="var(--orange)" stroke-width="1.6"/><path d="M2 5l10 8 10-8" fill="none" stroke="var(--orange)" stroke-width="1.6"/></svg>
    info@brookmereosteopathy.example</p>
  <p class="contact" style="top:1009px">
    <svg viewBox="0 0 24 24" aria-hidden="true"><g fill="none" stroke="var(--orange)" stroke-width="1.6"><circle cx="12" cy="12" r="10"/><ellipse cx="12" cy="12" rx="4.5" ry="10"/><path d="M2 12h20M4 7h16M4 17h16"/></g></svg>
    www.brookmereosteopathy.example</p>
</main>
</body>
</html>
```